Blue Harbor Car Finance Home Page

We need a desktop version mock up (we will base our mobile version off of this) of a website homepage for our auto loan business, Blue Harbor Car Finance. This does not need to be a functioning site, just a home page mock up. We are based in the metro St. Louis, MO area. We offer "guaranteed" auto loans for all credit types. We specialize in financing for bad/no credit customers. We are able to help rebuild these type of customers' credit, all while putting them in a great late model vehicle they'll love. Our online credit app takes less than 60 seconds, doesn't require a SS# and gives a free credit score if they fill it out within 3 minutes. We are looking for an outside perspective to help us in this design process. We are not completely sure what we want, but we do want it to be professional and secure looking, all while being unique and aesthetically pleasing. We want the customer to be able to put in their zip code to be directed to the right location that can get them pre approved. I attached a wireframe with some stuff we'd like to include, but in no way does it have to be in the same layout or the same ideas. We want everyone to "go crazy" with their creative side on this. Our current site is awful, here is a link to get a better idea: www.blueharborcarfinance-example.com. Attached is our logo too, base colors off of it. Watch our video that is also attached for a better idea.

Target Market(s)

Residents of the St. Louis Missouri Metro Area that need an auto loan. 24-55 Male and Female - Lots of "urban market" customers.

Industry/Entity Type

Loan

Number of Pages Required

1 page

Colors
9bcb3b

Requirements
Must have
• An area where the customer can enter their zip code - Be creative!
Nice to have
• See wireframe attachment for ideas - Be creative!

```html
<!DOCTYPE html>
<html lang="en">
<head>
<meta charset="utf-8">
<title>Blue Harbor Car Finance – Home</title>
<link rel="stylesheet" href="https://fonts.googleapis.com/css2?family=Open+Sans:ital,wght@0,400;0,600;0,700;1,400&display=swap">
<style>
:root{
  --green:#9bcb3b;
  --green-light:#b5ec4a;
  --green-dark:#86bb2c;
  --ink:#3a3a3a;
  --body:#555;
  --white:#fff;
  --footer:#333333;
  --footer-text:#bdbdbd;
}
*{margin:0;padding:0;box-sizing:border-box}
html,body{width:1200px;height:2497px;overflow:hidden}
body{font-family:"Open Sans",Arial,sans-serif;color:var(--body);background:var(--white);position:relative}
.abs{position:absolute}

/* header */
.site-header{position:absolute;left:0;top:0;width:1200px;height:115px;border-top:3px solid var(--green);background:var(--white)}
.brand{position:absolute;left:133px;top:34px;display:flex;align-items:center;gap:10px;font-weight:700;font-size:22px;color:#2f7d1f}
.brand-mark{width:26px;height:26px;background:var(--green)}
.main-nav{position:absolute;top:58px;left:503px;display:flex;font-size:12px;color:#333}
.main-nav a{color:inherit;text-decoration:none;position:absolute;white-space:nowrap}
.main-nav .sep{position:absolute;color:#333}
.main-nav .active{color:var(--green)}
.nav-underline{position:absolute;left:503px;top:109px;width:54px;height:5px;background:var(--green)}
.phone{position:absolute;left:940px;top:50px;display:flex;align-items:center;gap:13px;font-size:12px;color:#333}
.phone-icon{width:35px;height:35px;border-radius:50%;background:var(--green);display:flex;align-items:center;justify-content:center}

/* hero */
.hero{position:absolute;left:0;top:115px;width:1200px;height:451px;overflow:hidden}
.hero-photo{position:absolute;inset:0;background:linear-gradient(100deg,#4a4d52 0%,#8a8a88 25%,#b9a896 45%,#6b7f9a 70%,#2b2f36 100%)}
.hero-title{position:absolute;left:0;width:1200px;top:133px;text-align:center;color:var(--white);font-size:30px;font-weight:700;text-shadow:0 1px 3px rgba(0,0,0,.5)}
.hero-sub{position:absolute;left:0;width:1200px;top:177px;text-align:center;color:var(--white);font-size:16px;text-shadow:0 1px 2px rgba(0,0,0,.5)}
.zip-panel{position:absolute;left:411px;top:233px;width:378px;height:86px;background:rgba(255,255,255,.35)}
.zip-input{position:absolute;left:22px;top:20px;width:193px;height:45px;background:var(--white);border:0;font:12px "Open Sans",sans-serif;color:#555;padding-left:16px;display:flex;align-items:center}
.zip-btn{position:absolute;left:228px;top:20px;width:130px;height:45px;background:linear-gradient(var(--green-light),var(--green));color:var(--white);font-weight:700;font-size:14px;display:flex;align-items:center;justify-content:center}
.perks{position:absolute;left:809px;top:237px;list-style:none;color:var(--white);font-size:12.5px;font-weight:600}
.perks li{display:flex;align-items:center;gap:9px;height:22px}

/* apply band */
.apply-band{position:absolute;left:0;top:566px;width:1200px;height:88px;background:linear-gradient(var(--green-light),var(--green))}
.apply-label{position:absolute;left:371px;top:28px;font-size:20px;font-weight:700;color:var(--white)}
.timer{position:absolute;left:514px;top:25px;width:95px;height:36px;background:var(--white);font-size:13px;color:#333;display:flex;align-items:center;justify-content:center}
.apply-note{position:absolute;left:629px;top:34px;font-size:13px;color:var(--white)}

/* testimonial */
.testimonial{position:absolute;left:0;top:654px;width:1200px;height:206px;text-align:center}
.testimonial h2{position:absolute;left:0;width:1200px;top:26px;font-size:25px;font-weight:700;color:var(--ink)}
.testimonial blockquote{position:absolute;left:330px;width:540px;top:78px;font-size:12.5px;line-height:23px;color:var(--body)}
.testimonial cite{position:absolute;left:0;width:1200px;top:139px;font-size:12.5px;color:var(--green)}
.arrow{position:absolute;top:72px}

/* payment band */
.payment-band{position:absolute;left:0;top:860px;width:1200px;height:260px;overflow:hidden}
.payment-photo{position:absolute;inset:0;background:linear-gradient(95deg,#3d3a36 0%,#6d6257 40%,#8a7a6a 60%,#4a4540 100%)}
.payment-text{position:absolute;left:213px;width:400px;top:95px;text-align:center;color:var(--white);font-size:14.5px;line-height:22px}
.calc-btn{position:absolute;left:652px;top:95px;width:243px;height:57px;background:linear-gradient(var(--green-light),var(--green));color:var(--white);font-size:19px;font-weight:700;display:flex;align-items:center;justify-content:center}

/* steps */
.step-photo{position:absolute;width:210px;height:200px;border:1px solid #ddd;padding:5px;background:var(--white);box-shadow:0 1px 3px rgba(0,0,0,.15)}
.step-photo div{width:100%;height:100%}
.step-title{position:absolute;font-size:25px;font-weight:700;color:var(--ink)}
.step-text{position:absolute;width:400px;font-size:12.5px;line-height:22.5px;color:var(--body);text-align:justify}

/* about band */
.about-band{position:absolute;left:0;top:1998px;width:1200px;height:353px;background:linear-gradient(var(--green-light),var(--green-dark))}
.about-band h3{position:absolute;left:133px;top:92px;font-size:20px;font-weight:700;color:var(--white)}
.about-band p{position:absolute;left:133px;top:136px;width:400px;font-size:12.5px;line-height:22.5px;color:var(--white);text-align:justify}
.video-frame{position:absolute;left:609px;top:50px;width:406px;height:250px;background:var(--white);padding:10px;box-shadow:0 2px 5px rgba(0,0,0,.2)}
.video-still{width:100%;height:100%;background:linear-gradient(110deg,#9a8a80,#c7b8b2 50%,#7d6f78);position:relative}
.play{position:absolute;left:167px;top:87px}

/* footer */
.site-footer{position:absolute;left:0;top:2351px;width:1200px;height:146px;background:var(--footer);font-size:12px;color:var(--footer-text)}
.footer-nav a,.footer-nav span{position:absolute;top:32px;color:var(--white);text-decoration:none}
.footer-nav .active{color:var(--green)}
.copyright{position:absolute;left:0;width:1200px;top:65px;text-align:center}
.copyright b{font-weight:400;color:var(--green)}
.credit{position:absolute;left:0;width:1200px;top:92px;text-align:center}
</style>
</head>
<body>

<header class="site-header">
  <div class="brand"><span class="brand-mark"></span>Blue Harbor Car Finance</div>
  <nav class="main-nav">
    <a class="active" style="left:0">Locations</a>
    <span class="sep" style="left:72px">|</span>
    <a style="left:96px">Finance Center</a>
    <span class="sep" style="left:196px">|</span>
    <a style="left:221px">About</a>
    <span class="sep" style="left:275px">|</span>
    <a style="left:301px">FAQ</a>
    <span class="sep" style="left:341px">|</span>
    <a style="left:366px">Contact</a>
  </nav>
  <div class="nav-underline"></div>
  <div class="phone">
    <span class="phone-icon"><svg width="14" height="14" viewBox="0 0 24 24"><path fill="#fff" d="M6.6 10.8a15.1 15.1 0 0 0 6.6 6.6l2.2-2.2c.3-.3.7-.4 1-.2 1.1.4 2.3.6 3.6.6.6 0 1 .4 1 1V20c0 .6-.4 1-1 1A17 17 0 0 1 3 4c0-.6.4-1 1-1h3.5c.6 0 1 .4 1 1 0 1.3.2 2.5.6 3.6.1.3 0 .7-.2 1z"/></svg></span>
    1800 - 555 -0142
  </div>
</header>

<section class="hero">
  <div class="hero-photo" role="img" aria-label="Photo of a smiling couple receiving car keys from a salesman in a dealership showroom"></div>
  <h1 class="hero-title">Over 30,000 Auto Loans Since 2000</h1>
  <p class="hero-sub">Pre-Approval in Under 60 Seconds!</p>
  <div class="zip-panel">
    <div class="zip-input">Enter zip code</div>
    <div class="zip-btn">Get Approved</div>
  </div>
  <ul class="perks">
    <li><svg width="14" height="12" viewBox="0 0 14 12"><path d="M1 6.5l4 4L13 1.5" fill="none" stroke="#9bcb3b" stroke-width="3"/></svg>No Social Security Number Required</li>
    <li><svg width="14" height="12" viewBox="0 0 14 12"><path d="M1 6.5l4 4L13 1.5" fill="none" stroke="#9bcb3b" stroke-width="3"/></svg>Instant Approval</li>
    <li><svg width="14" height="12" viewBox="0 0 14 12"><path d="M1 6.5l4 4L13 1.5" fill="none" stroke="#9bcb3b" stroke-width="3"/></svg>No Application Fees</li>
    <li><svg width="14" height="12" viewBox="0 0 14 12"><path d="M1 6.5l4 4L13 1.5" fill="none" stroke="#9bcb3b" stroke-width="3"/></svg>All Credit Accepted</li>
  </ul>
</section>

<section class="apply-band">
  <span class="apply-label">Apply within</span>
  <span class="timer">3:00</span>
  <span class="apply-note">and see your credit score for free!</span>
</section>

<section class="testimonial">
  <h2>Testimonial</h2>
  <svg class="arrow" style="left:204px" width="14" height="24" viewBox="0 0 14 24"><path d="M12 2L2 12l10 10" fill="none" stroke="#444" stroke-width="2"/></svg>
  <blockquote>Lorem ipsum dolor sit amet, consectetur adipiscing elit. Proin a elit vitae erat accumsan venenatis in ecitur velit, dapibus fringilla!</blockquote>
  <cite>- Satised Customer -</cite>
  <svg class="arrow" style="left:956px" width="14" height="24" viewBox="0 0 14 24"><path d="M2 2l10 10L2 22" fill="none" stroke="#444" stroke-width="2"/></svg>
</section>

<section class="payment-band">
  <div class="payment-photo" role="img" aria-label="Darkened photo of a happy couple driving in a car"></div>
  <p class="payment-text">Lorem ipsum dolor sit amet, consectetur adipiscing elit. Proin a elit vitae erat accumsan.</p>
  <div class="calc-btn">Calculate Payment</div>
</section>

<section class="steps">
  <div class="step-photo" style="left:131px;top:1201px"><div role="img" aria-label="Illustration of a credit score checklist" style="background:linear-gradient(135deg,#e6e6e6,#b5b5b5)"></div></div>
  <h3 class="step-title" style="left:371px;top:1193px">Step 1</h3>
  <p class="step-text" style="left:371px;top:1240px">Lorem ipsum dolor sit amet, consectetur adipiscing elit. Proin a elit vitae erat accumsan venenatis in ecitur velit. dapibus fringilla. Nulla varius eleifend risus non scelerisque. Morbi sapien lorem, gravida in ex in, nibus scelerisque massa. Quisque in vulputate magna.</p>

  <div class="step-photo" style="left:857px;top:1456px"><div role="img" aria-label="Photo of hands holding a loan document near a laptop" style="background:linear-gradient(135deg,#d9d9d9,#f2eef0 50%,#a8a8ad)"></div></div>
  <h3 class="step-title" style="left:639px;width:200px;text-align:right;top:1448px">Step 2</h3>
  <p class="step-text" style="left:436px;top:1495px">Lorem ipsum dolor sit amet, consectetur adipiscing elit. Proin a elit vitae erat accumsan venenatis in ecitur velit. dapibus fringilla. Nulla varius eleifend risus non scelerisque. Morbi sapien lorem, gravida in ex in, nibus scelerisque massa. Quisque in vulputate magna.</p>

  <div class="step-photo" style="left:131px;top:1704px"><div role="img" aria-label="Photo of a salesman handing car keys to a couple beside a car" style="background:linear-gradient(135deg,#7d8088,#b9b2a8 50%,#3d4048)"></div></div>
  <h3 class="step-title" style="left:371px;top:1696px">Step 3</h3>
  <p class="step-text" style="left:371px;top:1743px">Lorem ipsum dolor sit amet, consectetur adipiscing elit. Proin a elit vitae erat accumsan venenatis in ecitur velit. dapibus fringilla. Nulla varius eleifend risus non scelerisque. Morbi sapien lorem, gravida in ex in, nibus scelerisque massa. Quisque in vulputate magna.</p>
</section>

<section class="about-band">
  <h3>Blue Harbor Car Finance</h3>
  <p>Lorem ipsum dolor sit amet, consectetur adipiscing elit. Proin a elit vitae erat accumsan venenatis in ecitur velit. dapibus fringilla. Nulla varius eleifend risus non scelerisque. Morbi sapien lorem, gravida in ex in, nibus scelerisque massa. Quisque in vulputate magna.</p>
  <div class="video-frame">
    <div class="video-still" role="img" aria-label="Video still of a couple reviewing bills at home">
      <svg class="play" width="56" height="56" viewBox="0 0 56 56"><circle cx="28" cy="28" r="26" fill="#111" stroke="#fff" stroke-width="3"/><path d="M22 16l17 12-17 12z" fill="#fff"/></svg>
    </div>
  </div>
</section>

<footer class="site-footer">
  <nav class="footer-nav">
    <a class="active" style="left:441px">HOME</a>
    <span style="left:499px">|</span>
    <a style="left:527px">ABOUT</a>
    <span style="left:589px">|</span>
    <a style="left:614px">PRIVACY</a>
    <span style="left:682px">|</span>
    <a style="left:707px">CONTACT</a>
  </nav>
  <p class="copyright">© 2016 <b>Blue Harbor Car Finance</b>. All Rights Reserved.</p>
  <p class="credit">Created by Northgate Web Studio.</p>
</footer>

</body>
</html>
```